Proposal Document Template for New Accounting and Tax Clients

Hi Farid,
We hope you are well.
We are an Accounting Firm based in the suburb of Pyrmont near Sydney city, and you recently designed a Package Title page for us that we use when providing our clients their year end statements and tax returns.

Because we like the design so much, we would like to work with you again. We would like you to incorporate aspects of your original Package Title Page design throughout our Proposal Document to provide design consistency between both documents.

We need our Proposal Document to be a fully editable Word document, as we send it to potential new clients to win their business and we will need to adjust what we include to suit each one.

We also think it could work if the design includes key images from our website.

We have two key brand colours:
Blue - Hex code #021738
Gold - Hex code #b2a98c

I have included:
- New Tormella Advisory Title Page_050225 - this was your previous design that we would like the Proposal Document to look similar to
- Proposal Document_V2_Detailed_Leo - this is our current Proposal Document that we would like you to redesign, keeping the content, but updating the design to look consistent with the New Tormella Advisory Title Page.
- Our Logo in different colours in JPEG Format (I also have PNG and EPS files of these. If you need them, please let me know)
- The key images from our website www.tormella.net.au

Please let me know if you have any questions or need anything further.

Thank you in advance
Jo
Updates

We received the designs one day ago, that combined with the Easter Holiday break means we need more time to review and provide feedback.

Target Market(s)

Accounting, Tax, and Strategic Business Planning Clients from Small Business, to Corporates , and Individuals

Industry/Entity Type

Accounting

Font styles to use
Other font styles liked:
• Calibri

Requirements
Must have
• Our logo and the ability to edit the document
Nice to have
• Include images from our website tormella.net.au

```html
<!DOCTYPE html>
<html lang="en">
<head>
<meta charset="utf-8">
<title>Tormella Advisory – Services Proposal</title>
<link rel="stylesheet" href="https://fonts.googleapis.com/css2?family=Poppins:wght@300;400;500;600;700;800&display=swap">
<style>
:root{
  --navy:#021738;
  --gold:#b2a98c;
  --canvas:#8a8a8a;
  --ink:#1d2333;
  --white:#ffffff;
  --rule:#c9c3ae;
}
*{box-sizing:border-box;margin:0;padding:0}
html,body{width:1200px;height:3119px;overflow:hidden}
body{background:var(--canvas);font-family:"Poppins",sans-serif;color:var(--ink);position:relative}
.sheet{position:absolute;width:414px;height:585px;background:var(--white);overflow:hidden;transform:scale(1.2109);transform-origin:0 0;box-shadow:0 1px 3px rgba(0,0,0,.25)}
.sheet--1{left:77.5px;top:76.3px}
.sheet--2{left:620px;top:76.3px}
.sheet--3{left:77.5px;top:829.5px}
.sheet--4{left:620px;top:829.5px}
.sheet--5{left:77.5px;top:1581.4px}
.sheet--6{left:620px;top:1581.4px}
.sheet--7{left:348.7px;top:2334.6px}
.shapes{position:absolute;inset:0;width:414px;height:585px}
.photo{position:absolute}
.heading{position:absolute;left:32px;top:40px;color:var(--navy);line-height:1.02;letter-spacing:.2px}
.heading .light{font-weight:500;display:block}
.heading .heavy{font-weight:800;display:block}
.heading .gold{color:var(--gold)}
.heading-rule{position:absolute;left:32px;height:1px;background:var(--navy)}
.heading-rule::before{content:"";position:absolute;left:0;top:-1px;width:30px;height:3px;background:var(--gold)}
.wordmark{position:absolute;font-weight:300;line-height:.85;letter-spacing:-.2px}
.wordmark span{display:block}
.wordmark span+span{padding-left:.45em}
.wordmark--white{color:var(--white)}
.wordmark--navy{color:var(--navy)}
.folio{position:absolute;left:30px;bottom:4px;width:9px;height:13px;background:var(--gold);color:var(--navy);font-size:5px;font-weight:600;text-align:center;line-height:15px;clip-path:polygon(0 20%,50% 0,100% 20%,100% 100%,0 100%)}
/* cover */
.cover-title{font-size:44px}
.cover-date{position:absolute;left:33px;top:466px;border:.6px solid var(--gold);color:var(--gold);font-size:6px;padding:1.5px 6px;letter-spacing:.3px}
.cover-contact{position:absolute;left:33px;color:var(--white);font-size:6.3px;line-height:1.35}
.cover-year{position:absolute;left:0;top:505px;font-size:76px;font-weight:800;color:var(--white);opacity:.05;letter-spacing:2px}
/* about */
.about-body{position:absolute;left:32px;top:146px;width:146px;font-size:7.8px;line-height:1.2;color:var(--ink)}
.about-body p+p{margin-top:9px}
.about-body b{font-weight:600}
/* team */
.team-col{position:absolute;top:132px;width:90px;height:224px;background:var(--gold)}
.team-member{position:absolute;width:74px;text-align:center}
.team-photo{width:74px;height:72px;border:2px solid var(--white);background:linear-gradient(160deg,#e6e6e6,#8f8f8f)}
.team-name{color:var(--white);font-size:8.5px;line-height:1.15;margin-top:9px}
/* proposal */
.prepared{position:absolute;left:32px;top:145px;font-size:7.6px;line-height:1.25;color:var(--ink)}
.lead{position:absolute;left:32px;top:198px;width:360px;font-size:7.6px;line-height:1.25}
.bio{position:absolute;left:45px;width:324px;height:96px;background:var(--gold)}
.bio-photo{position:absolute;left:12px;top:10px;width:76px;height:76px;border:2px solid var(--white);background:linear-gradient(160deg,#e9e9e9,#8c8c8c)}
.bio-text{position:absolute;left:100px;top:12px;width:212px;color:var(--white)}
.bio-name{font-size:7.2px;line-height:1.25}
.bio-name b{font-weight:600}
.bio-desc{font-size:6.1px;line-height:1.28;margin-top:8px;text-align:justify}
/* letter */
.letter{position:absolute;left:32px;top:44px;width:350px;font-size:6.8px;line-height:1.25;color:var(--ink)}
.letter p{margin-bottom:7px}
.letter .gap{margin-bottom:14px}
.ticks{list-style:none;margin:4px 0 8px 20px}
.ticks li{position:relative;padding-left:7px;margin-bottom:2.5px}
.ticks li svg{position:absolute;left:-6px;top:1px;width:6px;height:5px}
/* fees */
.fees{position:absolute;left:32px;top:34px;width:350px;font-size:6.8px;line-height:1.3}
.fees p{margin-bottom:8px}
.fees p b{font-weight:600}
table{border-collapse:collapse;font-size:5px;line-height:1.2}
.fee-table{margin:5px 0 12px 15px;width:320px;border:.6px solid var(--rule)}
.fee-table th,.rate-table th{background:var(--gold);color:var(--white);font-weight:500;text-align:left;padding:2.5px 6px;vertical-align:top}
.fee-table td{padding:3px 6px;border-top:.5px solid var(--rule);border-left:.5px solid var(--rule);vertical-align:top}
.fee-table tr.total td{background:var(--navy);color:var(--white);font-weight:600}
.fee-table td.note{font-size:4.8px}
.rate-table{margin:4px auto 12px;width:230px;border:.6px solid var(--rule)}
.rate-table td{padding:3px 6px;border-top:.5px solid var(--rule);border-left:.5px solid var(--rule)}
.signoff{position:absolute;left:32px;top:521px;font-size:6.8px}
/* acceptance */
.accept-title{position:absolute;left:32px;top:46px;font-size:10.5px;font-weight:700;color:var(--navy)}
.accept-lead{position:absolute;left:32px;top:64px;width:355px;font-size:6.8px;line-height:1.3}
.accept-table{position:absolute;top:92px;font-size:4.8px}
.accept-table th{background:var(--gold);color:var(--white);font-weight:500;text-align:left;padding:2px 6px}
.accept-table td{padding:1.4px 6px}
.box{display:inline-block;width:5px;height:5px;border:.5px solid #777;vertical-align:middle}
.sign{position:absolute;left:32px;font-size:6.6px}
.sign-line{position:absolute;width:82px;border-top:.6px dotted #666}
.sign-role{position:absolute;font-size:6.6px;width:82px;text-align:center}
.liability{position:absolute;left:40px;top:527px;width:334px;text-align:center;color:var(--white);font-size:7px;line-height:1.3}
</style>
</head>
<body>

<!-- Page 1: Cover -->
<section class="sheet sheet--1">
  <div class="photo" style="inset:0;background:linear-gradient(180deg,#8ea7c6 0%,#b9c4cf 38%,#6f7f8f 60%,#8a8074 80%,#5f5b55 100%)" role="img" aria-label="Photograph of a harbourside city skyline with towers, construction cranes and a tree"></div>
  <svg class="shapes" viewBox="0 0 414 585" preserveAspectRatio="none" aria-hidden="true">
    <polygon points="0,392 414,585 0,585" fill="#021738"/>
    <polygon points="180,476 414,378 414,585" fill="#ffffff"/>
  </svg>
  <div class="cover-year">2025</div>
  <h1 class="heading cover-title"><span class="light">SERVICES</span><span class="heavy">PROPOSAL</span></h1>
  <div class="cover-date">7 JANUARY 2025</div>
  <p class="cover-contact" style="top:484px">Address: Level 4, Suite 12,<br>88 Harbour Lane, Marlow Bay NSW 2031</p>
  <p class="cover-contact" style="top:511px">Call: +612 9000 4100&nbsp; | &nbsp;Visit: tormella.net.au</p>
  <div class="wordmark wordmark--navy" style="left:264px;top:466px;font-size:25px"><span>tormella</span><span>advisory</span></div>
</section>

<!-- Page 2: About -->
<section class="sheet sheet--2">
  <div class="photo" style="left:205px;top:0;width:209px;height:585px;background:linear-gradient(90deg,#2b2b2b,#9a9a9a 35%,#d8d8d8 60%,#5c5c5c)" role="img" aria-label="Black and white photograph of a modern apartment building facade"></div>
  <svg class="shapes" viewBox="0 0 414 585" preserveAspectRatio="none" aria-hidden="true">
    <polygon points="0,467 0,585 255,585" fill="#021738"/>
    <polygon points="150,537 195,500 195,558" fill="#b2a98c"/>
  </svg>
  <h1 class="heading" style="font-size:25.5px"><span class="light">ABOUT</span><span class="heavy">TORMELLA</span><span class="heavy gold">ADVISORY</span></h1>
  <div class="heading-rule" style="top:127px;width:137px"></div>
  <div class="about-body">
    <p>We are a boutique professional services firm focused on delivering customised accounting, tax and strategic business advice for our clients.</p>
    <p>We use our extensive chartered accounting and specialist tax experience to make your life easier by providing clear and concise advice on complex tax matters and business management.</p>
    <p>We pride ourselves on bringing life to numbers.</p>
    <p>We are trusted advisors to <b>small-to-medium enterprises</b> (SMEs), <b>Pacific Securities Exchange</b> (PSX) listed companies, local branches of <b>significant global entities</b> (SGEs), technology startups, and <b>High net worth individuals</b> (HNWI).</p>
  </div>
  <div class="wordmark wordmark--white" style="left:32px;top:528px;font-size:15px"><span>tormella</span><span>advisory</span></div>
  <div class="folio">2</div>
</section>

<!-- Page 3: Team -->
<section class="sheet sheet--3">
  <div class="photo" style="left:0;top:230px;width:414px;height:355px;background:linear-gradient(180deg,#ffffff 0%,#e9e6ea 20%,#d3d2d9 50%,#b8b9bf 75%,#8f9aa3 100%)" role="img" aria-label="Photograph of a cable-stayed harbour bridge and waterfront apartments at dusk"></div>
  <svg class="shapes" viewBox="0 0 414 585" preserveAspectRatio="none" aria-hidden="true">
    <polygon points="0,470 0,585 232,585" fill="#021738"/>
  </svg>
  <h1 class="heading" style="font-size:24px"><span class="light" style="display:inline">OUR </span><span class="heavy" style="display:inline">TEAM</span></h1>
  <div class="heading-rule" style="top:73px;width:137px"></div>
  <div class="team-col" style="left:44px"></div>
  <div class="team-col" style="left:162px"></div>
  <div class="team-col" style="left:279px"></div>
  <div class="team-member" style="left:52px;top:112px"><div class="team-photo" role="img" aria-label="Portrait of Leo Varnell"></div><p class="team-name">Leo Varnell</p></div>
  <div class="team-member" style="left:170px;top:112px"><div class="team-photo" role="img" aria-label="Portrait of Marcus Hale"></div><p class="team-name">Marcus<br>Hale</p></div>
  <div class="team-member" style="left:287px;top:112px"><div class="team-photo" role="img" aria-label="Portrait of Clara Benning"></div><p class="team-name">Clara Benning</p></div>
  <div class="team-member" style="left:52px;top:235px"><div class="team-photo" role="img" aria-label="Portrait of Rob Ashdown"></div><p class="team-name">Rob Ashdown</p></div>
  <div class="team-member" style="left:170px;top:235px"><div class="team-photo" role="img" aria-label="Portrait of Priya Ramesh"></div><p class="team-name">Priya<br>Ramesh</p></div>
  <div class="team-member" style="left:287px;top:235px"><div class="team-photo" role="img" aria-label="Portrait of Nora Castell"></div><p class="team-name">Nora Castell</p></div>
  <div class="wordmark wordmark--white" style="left:32px;top:528px;font-size:15px"><span>tormella</span><span>advisory</span></div>
  <div class="folio">3</div>
</section>

<!-- Page 4: Proposal intro -->
<section class="sheet sheet--4">
  <svg class="shapes" viewBox="0 0 414 585" preserveAspectRatio="none" aria-hidden="true">
    <polygon points="0,467 0,585 250,585" fill="#021738"/>
  </svg>
  <h1 class="heading" style="font-size:24px"><span class="light">PROPOSAL FOR</span><span class="heavy">OUTSOURCED CFO</span><span class="heavy gold">SERVICES</span></h1>
  <div class="heading-rule" style="top:126px;width:137px"></div>
  <p class="prepared">PREPARED FOR<br>Abc Limited<br>BY<br>Leo Varnell, Director, Tormella Advisory</p>
  <p class="lead">Leo Varnell will be the Tormella Advisory Director responsible for your affairs.<br>Should Leo not be available, your alternate contact will be Clara Benning.</p>
  <div class="bio" style="top:246px">
    <div class="bio-photo" role="img" aria-label="Portrait of Leo Varnell"></div>
    <div class="bio-text">
      <p class="bio-name"><b>Leo Varnell</b>, CA, CTA, Director</p>
      <p class="bio-desc">Leo has been a Chartered Accountant for 20 years. He specialises in complex tax matters, international tax and business valuations. Leo advises a number of significant clients, including Australia's third largest privately held technology company.</p>
    </div>
  </div>
  <div class="bio" style="top:359px">
    <div class="bio-photo" role="img" aria-label="Portrait of Clara Benning"></div>
    <div class="bio-text">
      <p class="bio-name"><b>Clara Benning</b>, CA, Director<br>Financial Reporting and CFO Services</p>
      <p class="bio-desc">Clara has been a Chartered Accountant for 20 years and manages a portfolio of corporate clients. She provides strategic advice, outsourced CFO and tax services to PSX Listed Companies.</p>
    </div>
  </div>
  <div class="wordmark wordmark--white" style="left:32px;top:528px;font-size:15px"><span>tormella</span><span>advisory</span></div>
  <div class="folio">4</div>
</section>

<!-- Page 5: Letter -->
<section class="sheet sheet--5">
  <svg class="shapes" viewBox="0 0 414 585" preserveAspectRatio="none" aria-hidden="true">
    <polygon points="0,469 0,585 266,585" fill="#021738"/>
    <polygon points="226,585 414,484 414,585" fill="#b2a98c"/>
  </svg>
  <div class="letter">
    <p class="gap">19 April 2025</p>
    <p class="gap">[insert name]<br>[insert company name]<br>Via email:</p>
    <p>Dear [salutation],</p>
    <p>PROPOSAL FOR ADVISORY SERVICES</p>
    <p>We are delighted to submit our proposal to Northwind Group for the provision of advisory services.</p>
    <p>Based on our discussions with you we have been asked to provide the following proposal:</p>
    <p style="margin-bottom:0">Our main objective is to provide you with:</p>
    <ul class="ticks">
      <li><svg viewBox="0 0 6 5"><path d="M.5 2.6 2.2 4.2 5.5.6" fill="none" stroke="#b2a98c" stroke-width=".9"/></svg>An independent review of your business forecasts and plans using Ledgerly data and Forecastly Predict software to assist with making business decisions with confidence</li>
      <li><svg viewBox="0 0 6 5"><path d="M.5 2.6 2.2 4.2 5.5.6" fill="none" stroke="#b2a98c" stroke-width=".9"/></svg>Comfort &amp; certainty to allow you to reward/draw an appropriate dividend based on the forecasted future cashflows of the business (3 months of expenses kept in cash)</li>
      <li><svg viewBox="0 0 6 5"><path d="M.5 2.6 2.2 4.2 5.5.6" fill="none" stroke="#b2a98c" stroke-width=".9"/></svg>We will do this by working with Karen and using Forecastly predict cashflow forecasting tool and providing you reports and meetings on an agreed schedule.</li>
    </ul>
    <p style="margin-bottom:0">Our scope includes:</p>
    <ul class="ticks">
      <li><svg viewBox="0 0 6 5"><path d="M.5 2.6 2.2 4.2 5.5.6" fill="none" stroke="#b2a98c" stroke-width=".9"/></svg>Initial needs analysis and client "deep dive," including understanding &amp; incorporating your current tools and plans into the software package.</li>
      <li><svg viewBox="0 0 6 5"><path d="M.5 2.6 2.2 4.2 5.5.6" fill="none" stroke="#b2a98c" stroke-width=".9"/></svg>Forecastly configuration and Ledgerly linking, (including input of budgets and forecasts prepared internally). Including calls and meetings as required.</li>
      <li><svg viewBox="0 0 6 5"><path d="M.5 2.6 2.2 4.2 5.5.6" fill="none" stroke="#b2a98c" stroke-width=".9"/></svg>Provision of training to Karen in Forecastly Product.</li>
      <li><svg viewBox="0 0 6 5"><path d="M.5 2.6 2.2 4.2 5.5.6" fill="none" stroke="#b2a98c" stroke-width=".9"/></svg>Quarterly Cashflow forecast reports to be provided, with alternative scenarios available.</li>
      <li><svg viewBox="0 0 6 5"><path d="M.5 2.6 2.2 4.2 5.5.6" fill="none" stroke="#b2a98c" stroke-width=".9"/></svg>Quarterly meetings (F2F or video call) to discuss the reports.</li>
      <li><svg viewBox="0 0 6 5"><path d="M.5 2.6 2.2 4.2 5.5.6" fill="none" stroke="#b2a98c" stroke-width=".9"/></svg>All calls/emails in respect of the project (except where part of agreed out of scope services)</li>
    </ul>
    <p style="margin-bottom:0">Agreed out of scope services include:</p>
    <ul class="ticks">
      <li><svg viewBox="0 0 6 5"><path d="M.5 2.6 2.2 4.2 5.5.6" fill="none" stroke="#b2a98c" stroke-width=".9"/></svg>Bookkeeping or data input and reconciliation services (Karen responsibility)</li>
      <li><svg viewBox="0 0 6 5"><path d="M.5 2.6 2.2 4.2 5.5.6" fill="none" stroke="#b2a98c" stroke-width=".9"/></svg>Tax and accountancy services provided under our earlier engagement letter</li>
      <li><svg viewBox="0 0 6 5"><path d="M.5 2.6 2.2 4.2 5.5.6" fill="none" stroke="#b2a98c" stroke-width=".9"/></svg>Additional meetings, additional scenarios or adjustments requested after meetings and subsequent reissuance of reports</li>
    </ul>
  </div>
  <div class="wordmark wordmark--white" style="left:32px;top:528px;font-size:15px"><span>tormella</span><span>advisory</span></div>
  <div class="folio">5</div>
</section>

<!-- Page 6: Fees -->
<section class="sheet sheet--6">
  <svg class="shapes" viewBox="0 0 414 585" preserveAspectRatio="none" aria-hidden="true">
    <polygon points="290,585 414,525 414,585" fill="#021738"/>
  </svg>
  <div class="fees">
    <p style="margin-bottom:0">Below is our <b>estimated fee</b> given our conversations:</p>
    <table class="fee-table">
      <tr><th style="width:42%">Task</th><th>Number per Year</th><th>Cost per Quarter (Ex GST)</th><th>Estimated Annual Cost (Ex GST)</th></tr>
      <tr><td>Preparation of Reports &amp; discussions with Karen/Northwind</td><td>4</td><td>$1,302.50</td><td>$5,210.00</td></tr>
      <tr><td>Quarterly Meetings</td><td>4</td><td>$995.50</td><td>$3,982.00</td></tr>
      <tr><td>KPI Review</td><td>4</td><td>$452.00</td><td>$1,808.00</td></tr>
      <tr class="total"><td>Total</td><td></td><td>$2,750.00</td><td>$11,000.00</td></tr>
      <tr><td class="note" colspan="4">In addition to the quarterly reports there will be a one-off setup &amp; configuration charge as listed in scope above which will also include training to Karen as appropriate</td></tr>
      <tr><td>Estimated setup costs</td><td>1</td><td></td><td>$2,500.00 - $3,500.00</td></tr>
    </table>
    <p>Our costs will be reviewed annually to ensure the fee is appropriate to the level of service required.</p>
    <p style="text-align:justify">It is our expectation that in the initial stages of our engagement, our time inputs will be higher than the long-term average that we have based our quote upon. We consider this our investment in the ongoing relationship as we work to understand your business and build best practice processes. We will endeavour to avoid out of scope charges to you as much as possible</p>
    <p>In acknowledgment of our learning curve, we respectfully request a minimum 6 month engagement. We have no doubt that at the end of the year you will be delighted with the service we have provided.</p>
    <p style="margin-bottom:0">The table below provides an indication of our team &amp; their <b>hourly rates</b> should you request additional services.</p>
    <table class="rate-table">
      <tr><th>Level of Expertise</th><th>Hourly Rates (Ex GST)</th></tr>
      <tr><td>Associate Director/Director</td><td>$350 – $515 Per hour</td></tr>
      <tr><td>Supervisor/Manager</td><td>$225 – $315 per hour</td></tr>
      <tr><td>Senior Accountant</td><td>$180 – $225 per hour</td></tr>
      <tr><td>Intermediate Accountant</td><td>$120 – $180 per hour</td></tr>
      <tr><td>Bookkeeper</td><td>$80 per hour</td></tr>
      <tr><td>Administration</td><td>$80 – $95 per hour</td></tr>
      <tr><td>Accounting Cadette</td><td>$70 per hour</td></tr>
    </table>
    <p>Should you have any queries or wish to discuss, please do not hesitate to contact me or Clara on <b>Telephone (02) 9000 4100 or Email clara@tormella.net.au.</b></p>
    <p>Yours sincerely,</p>
  </div>
  <p class="signoff">Leo Varnell, Director</p>
  <div class="wordmark wordmark--navy" style="left:293px;top:494px;font-size:15px"><span>tormella</span><span>advisory</span></div>
  <div class="folio">6</div>
</section>

<!-- Page 7: Acceptance -->
<section class="sheet sheet--7">
  <svg class="shapes" viewBox="0 0 414 585" preserveAspectRatio="none" aria-hidden="true">
    <polygon points="0,205 20,320 205,320 414,418 414,585 0,585" fill="#021738"/>
    <polygon points="312,372 414,300 414,414" fill="#b2a98c"/>
    <rect x="15" y="575" width="384" height="10" fill="#b2a98c"/>
  </svg>
  <h2 class="accept-title">Acceptance:</h2>
  <p class="accept-lead">I have read this proposal and I am pleased to accept the terms and conditions set out here in and attached.</p>
  <table class="accept-table" style="left:32px">
    <tr><th style="width:72px">CFO Services</th><th style="width:45px">Accepted</th></tr>
    <tr><td>Onboarding</td><td style="text-align:center"><span class="box"></span></td></tr>
    <tr><td>Weekly meetings</td><td style="text-align:center"><span class="box"></span></td></tr>
    <tr><td>Monthly meetings</td><td style="text-align:center"><span class="box"></span></td></tr>
    <tr><td>Appendix 4D</td><td style="text-align:center"><span class="box"></span></td></tr>
    <tr><td>Appendix 4E</td><td style="text-align:center"><span class="box"></span></td></tr>
    <tr><td style="white-space:nowrap">Audit committee meetings</td><td style="text-align:center"><span class="box"></span></td></tr>
    <tr><td>Ad-hoc attendances</td><td style="text-align:center"><span class="box"></span></td></tr>
  </table>
  <table class="accept-table" style="left:175px">
    <tr><th style="width:72px">Payroll Services</th><th style="width:45px">Accepted</th></tr>
    <tr><td>Weekly payroll</td><td style="text-align:center"><span class="box"></span></td></tr>
    <tr><td>Monthly payroll</td><td style="text-align:center"><span class="box"></span></td></tr>
  </table>
  <p class="sign" style="top:200px">Signed:</p>
  <p class="sign" style="top:216px">Name:</p>
  <div class="sign-line" style="left:77px;top:224px"></div>
  <div class="sign-line" style="left:192px;top:224px"></div>
  <p class="sign-role" style="left:77px;top:231px">Director</p>
  <p class="sign-role" style="left:192px;top:231px">Director</p>
  <p class="sign" style="top:264px">Date:</p>
  <div class="sign-line" style="left:77px;top:272px"></div>
  <div class="sign-line" style="left:192px;top:272px"></div>
  <p class="sign" style="top:282px">On acceptance we will send you our engagement letter.</p>
  <div class="wordmark wordmark--white" style="left:144px;top:462px;font-size:25px"><span>tormella</span><span>advisory</span></div>
  <p class="liability">Liability limited by a scheme approved under Professional Standards Legislation.</p>
</section>

</body>
</html>
```